Velbrixa - a brand new platform for targetted offers

Hello there, mockup forge!
As a new business we want to build a mobile web site (that later will be converted to mobile app) that will allow our customer to find great offers in their area provided by our partners.
What we'd like to get from you is a design of several mobile web site pages (screens). For the color choice we were considering unobtrusive combination of white, black and one of the extra colors: purple, green (shades ranging from green apple to mint) or cherry red. Most of the pages will contain images (offers) made by partners with unpredictable color combinations, so our main design should stay minimalist enough to keep customers attention to these images. The pages (screens) are as follows.
1. Welcome screen
- Product logo image
- Short text to thank customers for their choice
- Checkbox with text to accept Terms and Conditions (with link to them)
- Button to continue that is grayed out before the checkbox above is checked
2. List of offers (main screen)
- Header: search bar + 2 icon buttons: location button and menu button
- Info box with a link to profile screen to indicate that authorization is recommended
- Offers: a list of images headed with partner's icon and name aligned left and timer (clock icon + time) aligned right
- Menu: as it's planned, when menu button is pressed, a hover menu from the right is open to display a list of available screens
3. Partner's details and offers
- Header: Partner's name and back button
- Partner's full width logo image
- Short description text of a partner company (up to, say, 500 characters)
- Contact buttons with appropriate icons: "visit their web page" button, call button, location button, like/dislike buttons
- List of their offers as full-width images
- Selected offer should, also, show an "open-down" box with description aligned left and a button to use the offer aligned right
4. Favorites
- Header: Back button, screen name, filter button to open a hover screen to filter by location and other fields
- List of favorite partners with their icon and name aligned left and buttons to "subscribe"/"unsubscribe" (one button) and remove from favorites aligned right
5. Blacklist
- Same as favorites, with just "subscribe"/"unsubscribe" omitted
6. History
- List of taken offers displayed same way as on main screen with actual usage date instead of time remaining
7. Profile
- Header: Back button and screen name
- Rows of inputs for customer to define her age, gender, etc and/or authenticate by Chatterlane, QuilPost, etc.
8. Terms and Conitions
- Text of ToS
9. Language
- List of rows to choose a desired language
As this is our first try of MockupForge platform, please, don't hesitate to ask more questions or correct us on our order. If it feels like there are too many screens requested ahead, please, start with the first few with the intention to complete all of them when we choose you as a winner.
Thank you in advance for your cooperation!

```html
<!DOCTYPE html>
<html lang="en">
<head>
<meta charset="utf-8">
<title>Velbrixa – mobile screens</title>
<link href="https://fonts.googleapis.com/css2?family=Poppins:wght@400;500;600&family=Open+Sans:wght@400;600;700&display=swap" rel="stylesheet">
<style>
:root{
  --green:#79cc1e;
  --purple:#9c25b8;
  --board:#d8d8d8;
  --ink:#2b2b2b;
  --muted:#7a7a7a;
  --line:#dcdcdc;
  --foot:#ececec;
  --white:#ffffff;
}
*{box-sizing:border-box;margin:0;padding:0}
html,body{width:1200px;height:850px;overflow:hidden}
body{background:var(--board);font-family:"Open Sans",sans-serif;color:var(--ink);position:relative}
.screen{position:absolute;background:var(--white);overflow:hidden}
.app-bar{height:33px;background:var(--green);display:flex;align-items:center;justify-content:space-between;padding:0 12px 0 11px;position:relative}
.wordmark{font-family:"Poppins",sans-serif;font-weight:600;font-size:15px;color:var(--white);letter-spacing:.2px}
.menu-icon{width:19px;height:12px;display:flex;flex-direction:column;justify-content:space-between}
.menu-icon i{display:block;height:2px;background:var(--white)}
.abs{position:absolute}
.location{font-size:8px;color:#555;display:flex;align-items:center;gap:2px}
.location svg{width:7px;height:9px}
.footer{position:absolute;left:0;right:0;bottom:0;background:var(--foot);font-size:5.5px;color:#555;display:flex;align-items:center;justify-content:center}
.btn-green{background:var(--green);color:var(--white);border-radius:12px;font-size:7px;font-weight:600;display:flex;align-items:center;justify-content:center}
.section-title{font-family:"Poppins",sans-serif;font-size:12.5px;text-align:center;color:var(--ink)}
/* offer card */
.offer{position:absolute;left:9px;width:174px;border:1px solid var(--line);background:var(--white)}
.offer-photo{height:77px;position:relative;overflow:hidden}
.badge{position:absolute;left:-8px;top:-9px;width:38px;height:38px;border-radius:50%;background:var(--purple);color:var(--white);font-family:"Poppins",sans-serif;font-size:9px;line-height:9px;padding:12px 0 0 11px}
.badge small{display:block;font-size:6px;line-height:7px}
.offer-foot{height:41px;display:flex;align-items:center;justify-content:space-between;padding:0 7px 0 11px}
.partner b{display:block;font-family:"Poppins",sans-serif;font-weight:600;font-size:10.5px;line-height:12px;color:var(--ink)}
.partner span{display:block;font-size:6.5px;color:#333;margin-top:1px}
.timer{display:flex;gap:3px}
.timer div{width:22px;height:27px;border:1px solid var(--green);text-align:center;font-family:"Poppins",sans-serif;color:var(--purple);font-size:10.5px;line-height:14px;padding-top:2px}
.timer small{display:block;font-size:4.5px;line-height:6px;color:var(--green);font-family:"Open Sans",sans-serif}
.deal{text-align:right;font-family:"Poppins",sans-serif}
.deal small{display:block;font-size:6.5px;color:var(--green);line-height:8px}
.deal strong{font-size:10px;font-weight:600;color:var(--purple);line-height:11px}
.photo-shoes{background:linear-gradient(160deg,#cfc6bb 0%,#a88669 55%,#7a5a40 100%)}
.photo-sneaker{background:linear-gradient(135deg,#57c0ea 0%,#2f8fd1 100%)}
.photo-boots{background:linear-gradient(180deg,#6d5a4e 0%,#9c8570 60%,#c9bcae 100%)}
/* welcome */
.hero{position:absolute;left:0;right:0;top:74px;height:283px;background:linear-gradient(160deg,#eef0f2 0%,#dde3e8 60%,#cfd6dd 100%)}
.hero-title{position:absolute;left:0;right:0;top:108px;text-align:center;font-family:"Poppins",sans-serif;line-height:1}
.hero-title .big{font-size:23px;font-weight:500;display:block}
.hero-title .sub{font-size:15.5px;display:block;margin-top:1px}
.hero-copy{position:absolute;left:14px;right:14px;top:150px;text-align:center;font-size:6.2px;line-height:9.8px;color:#555}
.terms{position:absolute;left:0;right:0;top:238px;display:flex;justify-content:center;align-items:center;gap:4px;font-size:5.5px;color:#333}
.check{width:8px;height:8px;border:1px solid #777;background:var(--white);display:flex;align-items:center;justify-content:center}
/* menu */
.nav-list{position:absolute;left:0;right:0;top:44px}
.nav-list li{list-style:none;height:23px;display:flex;align-items:center;gap:7px;padding-left:15px;font-size:9px;color:#444;border-bottom:1px solid var(--line)}
.nav-list li:last-child{border-bottom:none}
.circle-arrow{width:11px;height:11px;border:1px solid #888;border-radius:50%;display:flex;align-items:center;justify-content:center}
.search{position:absolute;left:6px;top:41px;width:116px;height:15px;border:1px solid var(--line);border-radius:8px;font-size:5.5px;color:#999;padding:0 8px;display:flex;align-items:center;justify-content:space-between}
.info-box{position:absolute;left:15px;top:80px;width:166px;height:101px;border:1px solid var(--line);font-size:5.8px;line-height:10px;color:#555;text-align:center;padding:10px 14px}
/* partner detail */
.sub-bar{position:absolute;left:0;right:0;top:33px;height:27px;display:flex;align-items:center;justify-content:space-between;padding:0 9px 0 15px}
.sub-bar h2{font-family:"Poppins",sans-serif;font-weight:400;font-size:10.5px;color:#333}
.user{display:flex;align-items:center;gap:3px;font-size:5.5px;color:var(--white);position:absolute;left:100px;top:12px}
.avatar{width:11px;height:11px;border-radius:50%;background:#8a6a52}
.partner-card{position:absolute;left:10px;top:70px;width:173px;height:164px;border:1px solid var(--line)}
.partner-shoe{position:absolute;left:5px;top:6px;width:52px;height:46px;border-radius:6px;background:linear-gradient(135deg,#f26aa6,#d43d7e)}
.partner-card h3{position:absolute;left:65px;top:9px;font-family:"Poppins",sans-serif;font-weight:600;font-size:10px}
.partner-card p{position:absolute;left:65px;top:27px;width:99px;font-size:5.2px;line-height:7.3px;color:#777}
.actions{position:absolute;left:10px;top:138px;display:flex;gap:3px}
.actions .visit{width:70px;height:13px;border-radius:0;font-size:5px}
.sq{width:13px;height:13px;display:flex;align-items:center;justify-content:center}
.sq svg{width:8px;height:8px}
.sq.g{background:var(--green)}.sq.p{background:var(--purple)}
.detail-offer{position:absolute;left:10px;width:173px;border:1px solid var(--line);background:var(--white)}
.detail-offer .offer-photo{height:77px}
.detail-offer .offer-foot{height:35px;padding:0 10px 0 12px}
.pointer{position:absolute;left:84px;bottom:-5px;width:8px;height:8px;background:var(--purple);transform:rotate(45deg)}
.open-box{position:absolute;left:10px;top:629px;width:173px;height:69px;background:var(--purple);color:var(--white);font-size:5.2px;line-height:7.4px;padding:13px 72px 0 10px}
.open-box .cta{position:absolute;right:8px;top:17px;width:47px;height:15px;border:1px solid var(--white);border-radius:8px;font-size:6px;display:flex;align-items:center;justify-content:center}
/* favorites */
.back-btn{position:absolute;left:99px;top:11px;width:45px;height:13px;border:1px solid var(--white);border-radius:7px;color:var(--white);font-size:6px;display:flex;align-items:center;justify-content:center;gap:2px}
.filter-btn{width:54px;height:16px;border-radius:8px;font-size:6.5px}
.filter-box{position:absolute;left:14px;top:70px;width:166px;height:79px;border:1px solid var(--line);padding:9px 10px 0 10px}
.filter-row{display:flex;align-items:center;justify-content:space-between;height:20px;font-size:5.6px;color:#555}
.select{width:84px;height:14px;border:1px solid var(--line);font-size:5px;color:#777;padding:0 6px;display:flex;align-items:center;justify-content:space-between}
.fav-list{position:absolute;left:14px;top:164px;width:166px;border:1px solid var(--line)}
.fav-row{height:50px;display:flex;border-bottom:1px solid var(--line)}
.fav-row:last-child{border-bottom:none}
.fav-id{width:84px;border-right:1px solid var(--line);display:flex;flex-direction:column;align-items:center;justify-content:center;gap:4px}
.fav-id b{font-family:"Poppins",sans-serif;font-weight:600;font-size:10px}
.pill-purple{width:43px;height:11px;border-radius:6px;background:var(--purple);color:var(--white);font-size:5px;display:flex;align-items:center;justify-content:center}
.fav-act{flex:1;display:flex;align-items:center;justify-content:center}
.pill-outline{width:72px;height:14px;border:1px solid var(--green);border-radius:7px;color:var(--green);font-size:4.8px;display:flex;align-items:center;justify-content:center}
</style>
</head>
<body>
<svg width="0" height="0" style="position:absolute">
  <defs>
    <symbol id="pin" viewBox="0 0 10 14"><path d="M5 0C2.2 0 0 2.2 0 5c0 3.6 5 9 5 9s5-5.4 5-9C10 2.2 7.8 0 5 0zm0 7.2A2.2 2.2 0 1 1 5 2.8a2.2 2.2 0 0 1 0 4.4z" fill="#79cc1e"/></symbol>
    <symbol id="chev-right" viewBox="0 0 10 10"><path d="M4 2l3 3-3 3" fill="none" stroke="#888" stroke-width="1.2"/></symbol>
    <symbol id="chev-down" viewBox="0 0 10 10"><path d="M2 4l3 3 3-3" fill="none" stroke="#999" stroke-width="1.2"/></symbol>
    <symbol id="phone" viewBox="0 0 10 10"><path d="M2.2 1l1.6 2-1 1.1c.6 1.2 1.5 2.1 2.7 2.7l1.1-1 2 1.6-.9 1.6C4.8 9 1 5.2 1 1.9z" fill="#fff"/></symbol>
    <symbol id="pin-w" viewBox="0 0 10 14"><path d="M5 0C2.2 0 0 2.2 0 5c0 3.6 5 9 5 9s5-5.4 5-9C10 2.2 7.8 0 5 0zm0 7.2A2.2 2.2 0 1 1 5 2.8a2.2 2.2 0 0 1 0 4.4z" fill="#fff"/></symbol>
    <symbol id="up" viewBox="0 0 10 10"><path d="M1 9V5h2v4zm3 0V5l2-4c1 0 1.3.7 1.2 1.5L7 4h2l-.8 5z" fill="none" stroke="#fff" stroke-width=".9"/></symbol>
    <symbol id="down" viewBox="0 0 10 10"><path d="M1 1v4h2V1zm3 0v4l2 4c1 0 1.3-.7 1.2-1.5L7 6h2l-.8-5z" fill="none" stroke="#fff" stroke-width=".9"/></symbol>
    <symbol id="lens" viewBox="0 0 10 10"><circle cx="4.2" cy="4.2" r="3" fill="none" stroke="#777" stroke-width="1.1"/><path d="M6.4 6.4L9 9" stroke="#777" stroke-width="1.2"/></symbol>
  </defs>
</svg>

<!-- Screen 1: welcome -->
<section class="screen welcome" style="left:46px;top:24px;width:192px;height:382px;border-radius:18px">
  <header class="app-bar" style="height:50px;padding-top:14px">
    <span class="wordmark">Velbrixa</span>
    <span class="menu-icon"><i></i><i></i><i></i></span>
  </header>
  <div class="location abs" style="right:12px;top:56px"><svg><use href="#pin"/></svg>Location</div>
  <div class="hero" role="img" aria-label="Soft background photo of a person working on a laptop"></div>
  <h1 class="hero-title"><span class="big">Thank You</span><span class="sub">for Your choice</span></h1>
  <p class="hero-copy">Anim in massa libero interdum nec interdum vel blandit sed nulla in ullamcorper est eget tempor cursus neque mi consectetuer mi a ultricies massa est sed nisl class aptent taciti sociosqu ad litora torquent per conubia nostra per inceptos hymenaeos proin nulla arcu nonummy luctus dictum eget fermentum et lorem</p>
  <div class="terms"><span class="check"><svg width="6" height="6" viewBox="0 0 10 10"><path d="M1.5 5l2.5 2.5L8.5 2" fill="none" stroke="#444" stroke-width="1.6"/></svg></span>Accept Terms and Conditions</div>
  <div class="btn-green abs" style="left:73px;top:256px;width:65px;height:19px;font-size:8px">Submit</div>
  <footer class="footer" style="height:25px">© 2018 Company Name &nbsp;All right reserved</footer>
</section>

<!-- Screen 2: list of offers with menu -->
<section class="screen offers-menu" style="left:274px;top:26px;width:189px;height:653px">
  <header class="app-bar"><span class="wordmark">Velbrixa</span><span class="menu-icon"><i></i><i></i><i></i></span></header>
  <ul class="nav-list">
    <li><span class="circle-arrow"><svg width="7" height="7"><use href="#chev-right"/></svg></span>About Us</li>
    <li><span class="circle-arrow"><svg width="7" height="7"><use href="#chev-right"/></svg></span>Profile</li>
    <li><span class="circle-arrow"><svg width="7" height="7"><use href="#chev-right"/></svg></span>Partners</li>
    <li><span class="circle-arrow"><svg width="7" height="7"><use href="#chev-right"/></svg></span>Contact Us</li>
  </ul>
  <div class="abs" style="left:15px;top:164px;width:166px;height:17px;border:1px solid var(--line);border-top:none"></div>
  <div class="btn-green abs" style="left:66px;top:173px;width:65px;height:19px">Go to Profile</div>
  <h2 class="section-title abs" style="left:0;right:0;top:205px">List of Offers</h2>
  <article class="offer" style="top:230px">
    <div class="offer-photo photo-shoes" role="img" aria-label="Photo of leather shoes"><span class="badge">20%<small>OFF</small></span></div>
    <div class="offer-foot"><div class="partner"><b>Orvanta</b><span>Orvanta</span></div><div class="timer"><div>13<small>HRS</small></div><div>36<small>MIN</small></div><div>05<small>SEC</small></div></div></div>
  </article>
  <article class="offer" style="top:356px">
    <div class="offer-photo photo-sneaker" role="img" aria-label="Photo of sneakers on blue"><span class="badge">25%<small>OFF</small></span></div>
    <div class="offer-foot"><div class="partner"><b>Bidlane</b><span>Bidlane</span></div><div class="timer"><div>13<small>HRS</small></div><div>36<small>MIN</small></div><div>05<small>SEC</small></div></div></div>
  </article>
  <article class="offer" style="top:479px">
    <div class="offer-photo photo-boots" role="img" aria-label="Photo of boots and jeans"><span class="badge">30%<small>OFF</small></span></div>
    <div class="offer-foot"><div class="partner"><b>Marthaven</b><span>Marthaven</span></div><div class="timer"><div>13<small>HRS</small></div><div>36<small>MIN</small></div><div>05<small>SEC</small></div></div></div>
  </article>
  <footer class="footer" style="height:32px">© 2018 Company Name &nbsp;All right reserved</footer>
</section>

<!-- Screen 3: list of offers main -->
<section class="screen offers-main" style="left:506px;top:26px;width:189px;height:653px">
  <header class="app-bar"><span class="wordmark">Velbrixa</span><span class="menu-icon"><i></i><i></i><i></i></span></header>
  <div class="search">Search here<svg width="8" height="8"><use href="#lens"/></svg></div>
  <div class="location abs" style="left:137px;top:44px"><svg><use href="#pin"/></svg>Location</div>
  <div class="info-box">Anim in massa libero interdum nec interdum vel blandit sed nulla in ullamcorper est eget tempor cursus neque mi consectetuer mi a ultricies massa est sed nisl class aptent taciti sociosqu ad litora torquent per conubia nostra per inceptos hymenaeos proin nulla arcu nonummy luctus dictum eget fermentum et lorem</div>
  <div class="btn-green abs" style="left:66px;top:173px;width:65px;height:19px">Go to Profile</div>
  <h2 class="section-title abs" style="left:0;right:0;top:205px">List of Offers</h2>
  <article class="offer" style="top:230px">
    <div class="offer-photo photo-shoes" role="img" aria-label="Photo of leather shoes"><span class="badge">20%<small>OFF</small></span></div>
    <div class="offer-foot"><div class="partner"><b>Orvanta</b><span>Orvanta</span></div><div class="timer"><div>13<small>HRS</small></div><div>36<small>MIN</small></div><div>05<small>SEC</small></div></div></div>
  </article>
  <article class="offer" style="top:356px">
    <div class="offer-photo photo-sneaker" role="img" aria-label="Photo of sneakers on blue"><span class="badge">25%<small>OFF</small></span></div>
    <div class="offer-foot"><div class="partner"><b>Bidlane</b><span>Bidlane</span></div><div class="timer"><div>13<small>HRS</small></div><div>36<small>MIN</small></div><div>05<small>SEC</small></div></div></div>
  </article>
  <article class="offer" style="top:479px">
    <div class="offer-photo photo-boots" role="img" aria-label="Photo of boots and jeans"><span class="badge">30%<small>OFF</small></span></div>
    <div class="offer-foot"><div class="partner"><b>Marthaven</b><span>Marthaven</span></div><div class="timer"><div>13<small>HRS</small></div><div>36<small>MIN</small></div><div>05<small>SEC</small></div></div></div>
  </article>
  <footer class="footer" style="height:32px">© 2018 Company Name &nbsp;All right reserved</footer>
</section>

<!-- Screen 4: partner detail -->
<section class="screen partner-detail" style="left:734px;top:26px;width:190px;height:765px">
  <header class="app-bar"><span class="wordmark">Velbrixa</span><span class="user"><span class="avatar" role="img" aria-label="User avatar"></span>Rina Solt</span><span class="menu-icon"><i></i><i></i><i></i></span></header>
  <div class="sub-bar"><h2>ORVANTA</h2><span class="location"><svg><use href="#pin"/></svg>Location</span></div>
  <div class="partner-card">
    <div class="partner-shoe" role="img" aria-label="Photo of a pink sneaker"></div>
    <h3>Orvanta</h3>
    <p>Aenean vel congue id euismod in elit fusce ultricies orci ac feugiat suscipit leo massa sodales velit et scelerisque mi tortor at ipsum ligula augue bibendum accumsan vestibulum ut commodo a mi morbi ornare gravida elit integer congue augue et malesuada iaculis ipsum dui aliquet felis at cursus magna nisl nec elit praesent elementum elit at tellus nec ultricies sit amet porttitor mattis enim in massa libero interdum nec interdum vel blandit sed nulla in</p>
    <div class="actions">
      <span class="btn-green visit">Visit their web page</span>
      <span class="sq g"><svg><use href="#phone"/></svg></span>
      <span class="sq g"><svg viewBox="0 0 10 14"><use href="#pin-w"/></svg></span>
      <span class="sq p"><svg><use href="#up"/></svg></span>
      <span class="sq p"><svg><use href="#down"/></svg></span>
    </div>
  </div>
  <h2 class="section-title abs" style="left:0;right:0;top:243px;font-weight:500;font-size:11.5px">OFFERS</h2>
  <article class="detail-offer" style="top:262px">
    <div class="offer-photo photo-shoes" role="img" aria-label="Photo of leather shoes"></div>
    <div class="offer-foot"><div class="partner"><b>Orvanta</b><span>Orvanta</span></div><div class="deal"><small>GET NOW</small><strong>20 % OFF</strong></div></div>
  </article>
  <article class="detail-offer" style="top:388px">
    <div class="offer-photo photo-sneaker" role="img" aria-label="Photo of sneakers on blue"></div>
    <div class="offer-foot"><div class="partner"><b>Orvanta</b><span>Orvanta</span></div><div class="deal"><small>GET NOW</small><strong>25 % OFF</strong></div></div>
  </article>
  <article class="detail-offer" style="top:512px;box-shadow:0 2px 6px rgba(0,0,0,.15)">
    <div class="offer-photo photo-boots" role="img" aria-label="Photo of boots and jeans"></div>
    <div class="offer-foot" style="position:relative"><div class="partner"><b>Orvanta</b><span>Orvanta</span></div><div class="deal"><small>GET NOW</small><strong>30 % OFF</strong></div><span class="pointer"></span></div>
  </article>
  <div class="open-box">Aculis ipsum dui aliquet felis at cursus magna nisl nec elit praesent elementum elit at tellus nec ultricies sit amet porttitor mattis enim in massa libero interdum nec interdum vel blandit sed nulla in ullamcorper est eget tempor<span class="cta">Click here</span></div>
  <svg class="abs" style="left:88px;top:708px" width="14" height="10" viewBox="0 0 14 10"><path d="M1 2l6 6 6-6" fill="none" stroke="#888" stroke-width="1.4"/></svg>
  <footer class="footer" style="height:32px">© 2018 Company Name &nbsp;All right reserved</footer>
</section>

<!-- Screen 5: favorites -->
<section class="screen favorites" style="left:957px;top:26px;width:189px;height:472px">
  <header class="app-bar"><span class="wordmark">Velbrixa</span><span class="back-btn"><svg width="5" height="6" viewBox="0 0 6 10"><path d="M5 1L1 5l4 4" fill="none" stroke="#fff" stroke-width="1.3"/></svg>Back</span><span class="menu-icon"><i></i><i></i><i></i></span></header>
  <div class="sub-bar"><h2>Favorites</h2><span class="btn-green filter-btn abs" style="left:75px;top:6px">Filter</span><span class="location"><svg><use href="#pin"/></svg>Location</span></div>
  <div class="filter-box">
    <div class="filter-row">Filter by Location<span class="select">Location Title<svg width="6" height="6"><use href="#chev-down"/></svg></span></div>
    <div class="filter-row">Filter by Products<span class="select">Product<svg width="6" height="6"><use href="#chev-down"/></svg></span></div>
    <div class="filter-row">Filter by Offers<span class="select">Offers<svg width="6" height="6"><use href="#chev-down"/></svg></span></div>
  </div>
  <div class="fav-list">
    <div class="fav-row"><div class="fav-id"><b>Orvanta</b><span class="pill-purple">Subscribe</span></div><div class="fav-act"><span class="pill-outline">Remove from Favorites</span></div></div>
    <div class="fav-row"><div class="fav-id"><b>Bidlane</b><span class="pill-purple">Subscribe</span></div><div class="fav-act"><span class="pill-outline">Remove from Favorites</span></div></div>
    <div class="fav-row"><div class="fav-id"><b>Marthaven</b><span class="pill-purple">Subscribe</span></div><div class="fav-act"><span class="pill-outline">Remove from Favorites</span></div></div>
    <div class="fav-row"><div class="fav-id"><b>Kartquill</b><span class="pill-purple">Subscribe</span></div><div class="fav-act"><span class="pill-outline">Remove from Favorites</span></div></div>
    <div class="fav-row"><div class="fav-id"><b>Hemline</b><span class="pill-purple">Subscribe</span></div><div class="fav-act"><span class="pill-outline">Remove from Favorites</span></div></div>
  </div>
  <footer class="footer" style="height:30px">© 2018 Company Name &nbsp;All right reserved</footer>
</section>
</body>
</html>
```